The name of my company is Tolmen Refacing LLC and I would like the sub text to say "Cabinet Refacing and Countertops". Have my name Dorian Tolmen, Owner / Sales, contact info: Cell: 360-555-0147 / Email: dorian.tolmen@quenmail.com

Simple, Clean, and Organized. With colors that will appeal to the eye.

Target Market(s)

Houses and Apartments

Industry/Entity Type

Cabinet Refacing

Contact Information for Business Card

Company name and sub text Dorian Tolmen - Owner / Sales, my cell phone number and email

Requirements
Must have
• Business name, my name / position, and my contact info
Nice to have
• Simple. Organized. Appealing to the eye

```html
<!DOCTYPE html>
<html lang="en">
<head>
<meta charset="utf-8">
<title>Tolmen Refacing LLC — Business Card</title>
<link rel="stylesheet" href="https://fonts.googleapis.com/css2?family=Quicksand:wght@300;400&family=Montserrat:wght@700&family=Arimo:wght@400;700&display=swap">
<style>
  :root {
    --page-bg: #e4e4e2;
    --brand-blue: #446db4;
    --card-white: #ffffff;
    --charcoal: #353535;
    --ink-dark: #2b2b2b;
    --text-light: #ffffff;
  }
  * { margin: 0; padding: 0; box-sizing: border-box; }
  html, body {
    width: 1200px;
    height: 801px;
    overflow: hidden;
    background: var(--page-bg);
  }
  .canvas {
    position: relative;
    width: 1200px;
    height: 801px;
    display: flex;
    align-items: center;
    justify-content: center;
    gap: 40px;
  }
  .card {
    position: relative;
    width: 540px;
    height: 309px;
    overflow: hidden;
    box-shadow: 0 6px 18px rgba(0,0,0,0.18);
  }
  .card-front { background: var(--card-white); }
  .card-back { background: var(--brand-blue); }

  .front-shapes {
    position: absolute;
    inset: 0;
    width: 100%;
    height: 100%;
  }
  .shape-band { fill: var(--brand-blue); }
  .shape-corner { fill: var(--charcoal); }

  .company-name {
    font-family: "Quicksand", sans-serif;
    font-weight: 300;
    text-transform: uppercase;
    letter-spacing: 0.5px;
    line-height: 1;
    white-space: nowrap;
  }
  .company-tagline {
    font-family: "Montserrat", sans-serif;
    font-weight: 700;
    line-height: 1;
    white-space: nowrap;
  }

  .front-brand {
    position: absolute;
    left: 26px;
    top: 40px;
  }
  .front-brand .company-name {
    color: var(--brand-blue);
    font-size: 37px;
  }
  .front-brand .company-tagline {
    color: var(--ink-dark);
    font-size: 17px;
    margin-top: 8px;
    padding-left: 86px;
  }

  .contact-block {
    position: absolute;
    left: 26px;
    bottom: 22px;
    color: var(--text-light);
    font-family: "Arimo", sans-serif;
  }
  .contact-name {
    font-weight: 700;
    font-size: 20px;
    letter-spacing: 0.5px;
    text-transform: uppercase;
  }
  .contact-role {
    font-size: 13px;
    margin-top: 3px;
  }
  .contact-list {
    list-style: none;
    margin-top: 12px;
    font-size: 13px;
  }
  .contact-list li {
    display: flex;
    align-items: center;
    gap: 8px;
    margin-top: 4px;
  }
  .contact-icon {
    width: 12px;
    height: 12px;
    fill: none;
    stroke: var(--text-light);
    stroke-width: 1.4;
  }

  .back-brand {
    position: absolute;
    inset: 0;
    display: flex;
    flex-direction: column;
    align-items: center;
    justify-content: center;
    color: var(--text-light);
  }
  .back-brand .company-name { font-size: 38px; }
  .back-brand .company-tagline {
    font-size: 18px;
    margin-top: 8px;
  }
</style>
</head>
<body>
<main class="canvas">
  <section class="card card-front" aria-label="Business card front">
    <svg class="front-shapes" viewBox="0 0 540 309" preserveAspectRatio="none" aria-hidden="true">
      <polygon class="shape-band" points="0,196 540,40 540,309 0,309"/>
      <polygon class="shape-corner" points="410,0 540,0 540,28"/>
    </svg>

    <div class="front-brand">
      <h1 class="company-name">Tolmen Refacing, LLC</h1>
      <p class="company-tagline">Cabinets and Countertops</p>
    </div>

    <div class="contact-block">
      <p class="contact-name">Dorian Tolmen</p>
      <p class="contact-role">Owner / Sales</p>
      <ul class="contact-list">
        <li>
          <svg class="contact-icon" viewBox="0 0 12 12" aria-hidden="true">
            <path d="M2.5 1.5 L4.5 1.5 L5.2 4 L4 5 Q5 7 7 8 L8 6.8 L10.5 7.5 L10.5 9.5 Q6 10.5 3 7.5 Q1 5 2.5 1.5 Z"/>
          </svg>
          <span>360-555-0147</span>
        </li>
        <li>
          <svg class="contact-icon" viewBox="0 0 12 12" aria-hidden="true">
            <rect x="1" y="2.5" width="10" height="7"/>
            <polyline points="1,2.5 6,6.5 11,2.5"/>
          </svg>
          <span>dorian.tolmen@quenmail.com</span>
        </li>
      </ul>
    </div>
  </section>

  <section class="card card-back" aria-label="Business card back">
    <div class="back-brand">
      <p class="company-name">Tolmen Refacing, LLC</p>
      <p class="company-tagline">Cabinets and Countertops</p>
    </div>
  </section>
</main>
</body>
</html>
```